Updated DJ business Card showing other businesses

DJ Kestro offers professional mobile dj services including DJ. MC. Karaoke.
Silent Disco (will attach logo)
I also offer a 360 Photo Booth.

Contact info:
(555) 013-4472
marcus.tellgren@lumomail.net
Social Media @DJKestroNWX

```html
<!DOCTYPE html>
<html lang="en">
<head>
<meta charset="utf-8">
<title>DJ Kestro — Business Card</title>
<link href="https://fonts.googleapis.com/css2?family=Montserrat:wght@400;600;700;800&display=swap" rel="stylesheet">
<style>
  :root {
    --stage: #e9e5de;
    --card: #ffffff;
    --ink: #141414;
    --accent: #d81f4a;
    --muted: #3a3a3a;
    --ghost: #f1f1f1;
  }
  * { box-sizing: border-box; margin: 0; padding: 0; }
  html, body { width: 900px; height: 1200px; overflow: hidden; }
  body {
    background: var(--stage);
    font-family: "Montserrat", Arial, sans-serif;
    color: var(--ink);
    position: relative;
  }
  .card {
    position: absolute;
    left: 80px;
    width: 740px;
    height: 440px;
    background: var(--card);
    border-radius: 36px;
    box-shadow: 0 6px 10px rgba(0,0,0,0.35);
    overflow: hidden;
  }
  .card--front { top: 130px; }
  .card--back { top: 638px; }

  .wordmark {
    position: absolute;
    font-weight: 800;
    color: var(--ink);
    letter-spacing: -1px;
    line-height: 1;
    white-space: nowrap;
  }
  .card--front .wordmark { left: 42px; top: 66px; font-size: 66px; }

  .ghost-mark {
    position: absolute;
    right: -30px;
    top: 120px;
    font-size: 150px;
    font-weight: 800;
    color: var(--ghost);
    line-height: 1;
    white-space: nowrap;
    z-index: 0;
  }

  .identity { position: absolute; left: 40px; top: 266px; z-index: 1; }
  .identity__role { font-size: 25px; font-weight: 700; color: var(--accent); }
  .identity__title { font-size: 16px; color: var(--muted); margin-top: 2px; }

  .divider {
    position: absolute;
    left: 38px; right: 50px; top: 330px;
    height: 1.5px;
    background: var(--accent);
    z-index: 1;
  }

  .contacts { position: absolute; left: 38px; top: 340px; list-style: none; z-index: 1; }
  .contacts li {
    display: flex; align-items: center; gap: 8px;
    font-size: 16px; color: var(--muted); height: 23px;
  }
  .contacts svg { width: 15px; height: 15px; fill: var(--accent); flex: none; }
  .dot { width: 15px; height: 15px; border-radius: 50%; background: var(--accent); flex: none; }

  .card--back .wordmark {
    left: 0; right: 0; top: 88px;
    text-align: center;
    font-size: 96px;
  }
  .service {
    position: absolute;
    left: 0; right: 0; top: 250px;
    display: flex; align-items: center; justify-content: center; gap: 22px;
  }
  .service__circle {
    width: 96px; height: 96px; border-radius: 50%;
    background: var(--ink);
  }
  .service__name {
    font-size: 58px; font-weight: 800; color: var(--ink); letter-spacing: -1px;
    white-space: nowrap;
  }
</style>
</head>
<body>
  <section class="card card--front">
    <div class="ghost-mark" aria-hidden="true">KESTRO</div>
    <div class="wordmark">DJ KESTRO</div>
    <div class="identity">
      <p class="identity__role">MC. Karaoke</p>
      <p class="identity__title">Artist</p>
    </div>
    <div class="divider"></div>
    <ul class="contacts">
      <li>
        <svg viewBox="0 0 24 24" aria-hidden="true"><path d="M6.6 10.8a15.1 15.1 0 0 0 6.6 6.6l2.2-2.2a1 1 0 0 1 1-.25 11.4 11.4 0 0 0 3.6.57 1 1 0 0 1 1 1V20a1 1 0 0 1-1 1A17 17 0 0 1 3 4a1 1 0 0 1 1-1h3.5a1 1 0 0 1 1 1c0 1.25.2 2.45.57 3.6a1 1 0 0 1-.25 1z"/></svg>
        (555) 013-4472
      </li>
      <li>
        <svg viewBox="0 0 24 24" aria-hidden="true"><path d="M2 5h20v14H2z M2 5l10 8 10-8" fill="none" stroke="#d81f4a" stroke-width="2.4"/></svg>
        marcus.tellgren@lumomail.net
      </li>
      <li>
        <span class="dot" aria-hidden="true"></span>
        @DJKestroNWX
      </li>
    </ul>
  </section>

  <section class="card card--back">
    <div class="wordmark">DJ KESTRO</div>
    <div class="service">
      <span class="service__circle" aria-hidden="true"></span>
      <span class="service__name">Silent Disco</span>
    </div>
  </section>
</body>
</html>
```